Book Cover - Life Lessons Book

I have written a book for my sons who are graduating high school and college. Working title is "Chart Your Compass.....38 Lessons Learned at Home" I am looking for the book to appeal to young adults and parents who would want to give this book to them. It is a 125 page book that will be hardback and paperback - probably 5x8 or 6x9.
Updates

Reason: Altered some of the design elements based on the first submissions received. Would really like to have designs by Monday, May 15, 2016 but could not force a 2 day extension.

Target Market(s)

Young adults -- graduates, 20-3- year olds. And, parents would would give a book to their kids

Industry/Entity Type

Book Publisher

Font styles to use
Serif

Requirements
Must have
• Great design. It is a book cover so needs to catch the attention.
Nice to have
• I am open to more animated/playful/modern look or a more traditional look. Just would like to appeal to young adults and parents.
Should not have
• Anything in poor taste

```html
<!DOCTYPE html>
<html lang="en">
<head>
<meta charset="UTF-8">
<title>Chart Your Compass – Book Cover</title>
<link rel="stylesheet" href="https://fonts.googleapis.com/css2?family=Old+Standard+TT:wght@400;700&family=Oswald:wght@600&family=Playfair+Display:wght@400;700&display=swap">
<style>
  :root {
    --backdrop: #3a3a3a;
    --cover-black: #000000;
    --band-yellow: #e9b42c;
    --band-ink: #1a1a1a;
    --author-lime: #c8cc35;
    --label-grey: #d8d8d8;
    --title-white: #ffffff;
    --sky-night: #0f2a45;
    --sky-deep: #1d5663;
    --sky-mid: #5a9ba3;
    --sky-light: #b4d6d6;
    --ground: #050807;
  }
  * { margin: 0; padding: 0; box-sizing: border-box; }
  html, body {
    width: 1200px;
    height: 1000px;
    overflow: hidden;
    background: var(--backdrop);
  }
  .canvas {
    position: relative;
    width: 1200px;
    height: 1000px;
  }
  .cover {
    position: absolute;
    left: 310px;
    top: 58px;
    width: 580px;
    height: 927px;
    background: var(--cover-black);
    overflow: hidden;
  }
  .subtitle-band {
    position: absolute;
    left: 0;
    top: 0;
    width: 580px;
    height: 96px;
  }
  .subtitle-band svg { position: absolute; inset: 0; }
  .subtitle {
    position: absolute;
    left: 0;
    top: 20px;
    width: 100%;
    text-align: center;
    font-family: "Old Standard TT", serif;
    font-weight: 700;
    font-size: 28px;
    letter-spacing: 0;
    color: var(--band-ink);
    transform: scaleY(1.15);
  }
  .author-label {
    position: absolute;
    top: 86px;
    width: 100%;
    text-align: center;
    font-family: "Playfair Display", serif;
    font-size: 9px;
    letter-spacing: 1px;
    color: var(--label-grey);
  }
  .author-name {
    position: absolute;
    top: 104px;
    width: 100%;
    text-align: center;
    font-family: "Old Standard TT", serif;
    font-size: 44px;
    letter-spacing: 4px;
    color: var(--author-lime);
  }
  .cover-photo {
    position: absolute;
    left: 0;
    top: 174px;
    width: 580px;
    height: 452px;
    background:
      linear-gradient(180deg, rgba(5,8,7,0) 88%, var(--ground) 96%),
      radial-gradient(ellipse 45% 22% at 30% 30%, rgba(200,228,228,0.75) 0%, rgba(200,228,228,0) 100%),
      radial-gradient(ellipse 50% 18% at 60% 55%, rgba(180,214,214,0.55) 0%, rgba(180,214,214,0) 100%),
      radial-gradient(ellipse 30% 12% at 90% 72%, rgba(210,232,232,0.6) 0%, rgba(210,232,232,0) 100%),
      radial-gradient(ellipse 60% 40% at 100% 0%, var(--sky-night) 0%, rgba(15,42,69,0) 100%),
      linear-gradient(180deg, var(--sky-mid) 0%, var(--sky-light) 40%, var(--sky-mid) 70%, var(--sky-deep) 88%);
  }
  .title {
    position: absolute;
    left: 0;
    width: 100%;
    text-align: center;
    color: var(--title-white);
  }
  .title-top {
    top: 634px;
    font-family: "Playfair Display", serif;
    font-weight: 400;
    font-size: 80px;
    letter-spacing: 10px;
  }
  .title-joiner {
    top: 740px;
    font-family: "Old Standard TT", serif;
    font-weight: 700;
    font-size: 14px;
    letter-spacing: 2px;
  }
  .title-bottom {
    top: 750px;
    font-family: "Oswald", sans-serif;
    font-weight: 600;
    font-size: 78px;
    letter-spacing: -1px;
  }
</style>
</head>
<body>
<main class="canvas">
  <article class="cover">
    <header class="subtitle-band">
      <svg width="580" height="96" viewBox="0 0 580 96" aria-hidden="true">
        <path fill="var(--band-yellow)" d="M0 0 H580 V62 L562 66 L548 60 L530 70 L505 63 L488 74 L470 64 L450 69 L428 62 L410 75 L392 66 L370 71 L350 63 L332 72 L310 65 L290 78 L270 66 L250 71 L228 63 L210 76 L190 67 L170 72 L150 62 L130 74 L110 65 L92 70 L72 63 L55 77 L38 66 L20 71 L0 64 Z"/>
        <path fill="var(--band-yellow)" d="M60 72 L140 70 L138 74 L62 76 Z M300 74 L420 72 L418 75 L302 78 Z M470 70 L540 68 L538 72 L472 73 Z" opacity="0.7"/>
      </svg>
      <p class="subtitle">38 LESSONS LEARNED AT HOME</p>
    </header>
    <p class="author-label">AUTHOR</p>
    <p class="author-name">AUTHOR NAME</p>
    <div class="cover-photo" role="img" aria-label="Photo of a person's silhouette leaping across a grassy hilltop against a cloudy teal sky"></div>
    <h1>
      <span class="title title-top">CHART</span>
      <span class="title title-joiner">YOUR</span>
      <span class="title title-bottom">COMPASS</span>
    </h1>
  </article>
</main>
</body>
</html>
```